A4 Poster Design for Kowhai Racquet School

The Kowhai Racquet School is a premium tennis academy for beginners to advanced players in the Waikato. We offer tennis lessons and coaching to high performance youth, as well as adults and beginner kids in the Waikato.Our coaches; Tobias, Frederic and Maria; have more than 40 years of coaching experience between them. They have played at the elite level and have a great passion for teaching tennis to both top players as well as those new to tennis.We focus on quality, not quantity. You or your kids will receive the best tennis coaching in NZ right from the beginning. Our KRS players have won 21 national titles in singles and 37 national titles in doubles. More than 25 of our players have received a scholarship to universities in the USA. Our programme is complete with technical, tactical and physical training, match play and the opportunity to travel within NZ, and to Australia and France. We would like an A4 Poster that we can put up on noticeboards and hand out at tennis centres. We know there is a lot of text to include but we are hoping that you'll still be able to make it look good. The Unique Selling Point is that the KRS is NZ's best tennis academy. Please include the KRS logo. We would like to see designs that are similar to the look of our website. Please go to www.kowhairacquetschool.example.nz for more info. We have included some pics to personalise it. Please choose the ones that you think look good, you do not need to use all of them or any of them if you think the design is good enough on it's own. I can send through more pics if needed including any of the ones off the website.

Target Market(s)

tennis players and parents of tennis players

Font styles to use
Sans Serif

Requirements
Must have
• KRS logo
Nice to have
• photos

```html
<!DOCTYPE html>
<html lang="en">
<head>
<meta charset="utf-8">
<title>Kowhai Racquet School – Premium tennis coaching</title>
<link rel="stylesheet" href="https://fonts.googleapis.com/css2?family=Arimo:wght@400;700&display=swap">
<style>
  :root {
    --page: #ffffff;
    --sky: #b9c6cf;
    --trees: #1f2a1c;
    --trees-mid: #2c3a27;
    --court: #3f6a4a;
    --court-light: #5f8d6a;
    --panel: rgba(8, 12, 8, 0.62);
    --panel-edge: rgba(255, 255, 255, 0.35);
    --text: #ffffff;
    --logo-bg: #ffffff;
    --logo-ink: #1b1b1b;
  }
  * { margin: 0; padding: 0; box-sizing: border-box; }
  html, body { width: 1200px; height: 900px; overflow: hidden; background: var(--page); }
  body { font-family: "Arimo", Arial, sans-serif; color: var(--text); font-weight: 700; }

  .poster { position: absolute; left: 303px; top: 0; width: 592px; height: 900px; overflow: hidden; }
  .poster-photo {
    position: absolute; inset: 0;
    background:
      radial-gradient(ellipse 60% 18% at 55% 4%, var(--sky), transparent 70%),
      linear-gradient(180deg, #6f7c76 0%, var(--trees-mid) 10%, var(--trees) 30%, #18201a 45%, var(--court) 62%, var(--court-light) 80%, var(--court) 100%);
  }
  .panel {
    position: absolute; left: 32px; top: 27px; width: 531px; height: 845px;
    background: var(--panel); border: 1px solid var(--panel-edge);
  }

  .headline { position: absolute; left: 42px; top: 30px; width: 515px; text-align: center; }
  .headline h1 { font-size: 38.5px; line-height: 44px; letter-spacing: 0.2px; }
  .headline h2 { font-size: 22.5px; line-height: 28px; }

  .intro { position: absolute; left: 40px; top: 110px; width: 516px; font-size: 12px; line-height: 12.1px; letter-spacing: -0.15px; }
  .intro p { margin-bottom: 12px; }
  .intro .tight { margin-bottom: 0; }
  .intro h3 { font-size: 12px; font-weight: 700; }

  .squads { position: absolute; left: 41px; top: 404px; width: 512px; }
  .squads h3 { font-size: 15px; line-height: 18px; margin-bottom: 3px; }
  .squads p { font-size: 8px; line-height: 11.6px; }

  .block { position: absolute; font-size: 8px; line-height: 9.3px; }
  .block h4 { font-size: 14.5px; line-height: 16px; margin-bottom: 2px; }
  .block .gap { margin-top: 9px; }
  .junior { left: 41px; top: 511px; width: 208px; }
  .elite { left: 325px; top: 511px; width: 212px; }
  .invitational { left: 41px; top: 707px; width: 212px; }
  .adults { left: 325px; top: 707px; width: 212px; }
  .private { left: 325px; top: 753px; width: 220px; }

  .brand {
    position: absolute; left: 41px; top: 791px; width: 164px; height: 71px;
    background: var(--logo-bg); display: flex; align-items: center; justify-content: center; gap: 10px;
  }
  .brand-mark { width: 14px; height: 14px; background: var(--logo-ink); }
  .brand-name { color: var(--logo-ink); font-size: 30px; font-weight: 700; letter-spacing: 3px; }
</style>
</head>
<body>
<main class="poster">
  <div class="poster-photo" role="img" aria-label="Blurred photograph of an outdoor tennis court with trees and sky behind"></div>
  <div class="panel"></div>

  <header class="headline">
    <h1>Premium tennis coaching</h1>
    <h2>for beginners to advanced in the Waikato</h2>
  </header>

  <section class="intro">
    <p>At the Kowhai Racquet School we offer tennis lessons and coaching to high performance youth, as well as adults and beginner kids in the Waikato.<br>
    Our coaches; Tobias, Frederic and Maria; have more than 40 years of coaching experience between them. They have played at the elite level and have a great passion for teaching tennis to both top players as well as those new to tennis.<br>
    We focus on quality, not quantity. You or your kids will receive the best tennis coaching in NZ right from the beginning.</p>
    <p>Our KRS players have won 21 national titles in singles and 37 national titles in doubles. More than 25 of our players have received a scholarship to universities in the USA.</p>
    <p>Our program is complete with technical, tactical and physical training, match play and the opportunity to travel within NZ, and to Australia and France.<br>
    If you would like to learn to play tennis, or improve your match play and fitness then please check out the information below or on our website and then get in touch. We'd love to hear from you.</p>
    <h3>HOT SHOTS</h3>
    <p class="tight">A programme for beginners, from 5 to 10 years old. We use softer balls and smaller courts and teach the best technique when it is easiest for the kids to learn. One hour session and racquets are provided.<br>
    Monday 4-5 pm and 5-6pm Kahu street $95</p>
  </section>

  <section class="squads">
    <h3>OUR SQUADS:</h3>
    <p>Mondays, Tuesdays and Thursdays are our squad days with 20 to 30 minutes of fitness per session.<br>
    Wednesday is our match play day with Junior and Elite squads together.<br>
    We are now using the smart sensor by Vantor to improve technique and also ClipCam to improve game plan and body language during matches.<br>
    On Fridays we work on serves, returns and do video analysis. This is followed by a Thai kick boxing with Rawiri Dunn (former world champion) to improve footwork and attitude.</p>
  </section>

  <section class="block junior">
    <h4>JUNIOR SQUAD</h4>
    <p>This is the next step after Hot Shots for those who are keen to play at least twice a week. Focus and technique, tactics with an increase in fitness. Sessions are 1h45 long. Sessions available every day of the week with a decrease in cost if you do more than one day. Cost is for the term.<br>
    1 session per week, $235<br>2 sessions $355<br>3 sessions $465<br>4 sessions $550<br>5 sessions $630</p>
    <p class="gap">Monday 6.15 to 8pm<br>Tuesday 4 to 5.45pm<br>Wednesday 4 to 5.30pm (Match Play)<br>Thursday 5 to 6.45pm<br>Friday 4 to 5.30pm</p>
  </section>

  <section class="block elite">
    <h4>ELITE SQUAD</h4>
    <p>For players who are playing tournaments, the emphasis is on strategy, fitness and match situation. Rally control is essential and players must play at least 6 tournaments per year.<br>
    1 session $295<br>2 sessions $445<br>3 sessions $595<br>4 sessions $695<br>5 sessions $750</p>
    <p class="gap">Monday 4-6.15pm<br>Tuesday 5.15-7.30pm<br>Wednesday 4-6.30pm (Match Play)<br>Thursday 4.30-6.45pm St Aidans school<br>Friday 7-8.30am</p>
  </section>

  <section class="block invitational">
    <h4>INVITATIONAL SQUAD</h4>
    <p>$245 (cost is different for this group with a maximum of 4 players per coach)<br>Friday 4-5.30pm</p>
  </section>

  <section class="block adults">
    <h4>ADULTS</h4>
    <p>Group lessons 3 to 6 players, $15 to $25 per player per hour.</p>
  </section>

  <section class="block private">
    <h4>PRIVATE LESSONS</h4>
    <p>Available for all<br>One hour $65<br>8 one hour sessions $460<br>$10 per hour extra if indoors</p>
    <p class="gap">admin@kowhairacquetschool.example.nz<br>www.kowhairacquetschool.example.nz</p>
  </section>

  <div class="brand">
    <span class="brand-mark"></span>
    <span class="brand-name">KRS</span>
  </div>
</main>
</body>
</html>
```